依頼詳細
当会議が主催する講演会のチラシ製作をお願いいたします。
載せていただきたい事項は記載項目のとおりです。

【デザイン等について】
・昨年のチラシを添付しますので、参考にしてください。
・デザイン、レイアウト、色合いなどは全てお任せします
・昨年のデザインは堅苦しい印象がありましたので、今年はもう少し自由度のあるデザインを希望いたします。
・PRの強化に繋がるような、分かりやすく、且つ講演会に行きたくなる、目を引くようなデザインにしていただけたら幸いです。
・講師の写真を1枚載せてください(添付の写真データを使用願います)
・A4 縦 フルカラー
記載項目
キャッチコピー:地方の実情に合った新幹線の在り方について学ぼう

講演:「白峰新幹線実現の可能性を探る~在来線、ミニ新幹線からフル規格の新幹線へ~」

講師:鉄道ジャーナリスト 柴田 亮 氏

とき:平成28年7月5日(火) 午後3時~

ところ:桐ヶ丘グランドホテル
桐ヶ丘市松葉町二丁目3番4号

主催:北辰新幹線青葉延伸推進会議

お問い合わせ:北辰新幹線青葉延伸推進会議事務局(桐ヶ丘市役所企画課内)
Tel 0199-42-8670

※「申込不要・入場無料」の文言を入れてください。
サイズ
A4
ページ数
片面
希望イメージ
シンプル 複雑
単色 カラフル
暗い 明るい
日常 高級
遊び心 厳粛
未来的 伝統的
女性的 男性的
希望する色
納品ファイル
• イラストレーター形式 (.ai)
補足説明
※イラストレーターファイルはアウトライン必須、カラーモードはCMYKで納品願います。
※PDF形式も納品願います。
※納品は電子メール形式でお願いします。
※提案いただいたデザインの中から必ずコンペの当選者を選定します。(内容によっては修正をお願いする場合があります)
※ 募集期間を6月15日(水)としておりましたが、提案件数が希望数に達したため、誠に勝手ながら、6月14日(火)の正午をもって締め切りとさせていただく予定ですのでご了承ください。

明るく、非常に分かりやすいデザインであり、やわらかくかつポップなデザインが気に入りました。

この度は素敵なデザインを提案していただき誠にありがとうございました。
クラウドソーシングのサービスを今回初めて利用させていただきましたが、スピーディーでかつ素晴らしいデザインを提案いただき正直驚きました。想像していた以上のデザインで非常にうれしく思っております。今後ともどうか一つよろしくお願いいたします。

```html
<!DOCTYPE html>
<html lang="ja">
<head>
<meta charset="utf-8">
<title>白峰新幹線 講演会</title>
<link href="https://fonts.googleapis.com/css2?family=Noto+Sans+JP:wght@400;500;700;900&family=Noto+Serif+JP:wght@700;900&display=swap" rel="stylesheet">
<style>
:root{
  --sky-top:#3f8fd0;
  --sky-mid:#a9d6ef;
  --field:#8dbf3a;
  --field-deep:#5f9a25;
  --navy:#123f7a;
  --green:#2f8f3a;
  --orange:#ef7d1a;
  --ink:#222;
  --white:#fff;
}
*{margin:0;padding:0;box-sizing:border-box}
html,body{width:848px;height:1200px;overflow:hidden;background:#fff}
body{font-family:"Noto Sans JP",sans-serif;color:var(--ink)}
.flyer{position:relative;width:848px;height:1200px;overflow:hidden}
.scenery{position:absolute;inset:0 0 auto 0;height:760px;
  background:linear-gradient(180deg,var(--sky-top) 0%,var(--sky-mid) 38%,#d9ecd0 52%,var(--field) 64%,var(--field-deep) 100%)}
.route-map{position:absolute;left:0;top:0;width:200px;height:1200px;
  background:linear-gradient(180deg,rgba(255,255,255,.55) 0%,rgba(232,244,236,.8) 60%,rgba(225,238,248,.9) 100%)}
.catch{position:absolute;right:20px;top:24px;writing-mode:vertical-rl;
  font-family:"Noto Serif JP",serif;font-weight:900;font-size:40px;line-height:1.35;
  color:var(--white);letter-spacing:.06em;text-shadow:0 2px 6px rgba(0,40,90,.45)}
.venue-map{position:absolute;left:241px;top:2px;width:310px;height:310px;border-radius:50%;
  background:#fff;border:6px solid var(--white);box-shadow:0 4px 14px rgba(0,0,0,.25);overflow:hidden}
.venue-map .label{position:absolute;top:26px;left:0;right:0;text-align:center;font-weight:700;font-size:20px;color:var(--white)}
.venue-map .label span{background:var(--navy);padding:3px 16px;border-radius:14px}
.venue-map .area{position:absolute;left:30px;right:30px;top:66px;bottom:30px;border-radius:12px;
  background:linear-gradient(180deg,#eef1f3,#dde3e8)}
.free-badge{position:absolute;left:462px;top:172px;width:86px;height:86px;border-radius:50%;
  background:var(--orange);color:var(--white);display:flex;flex-direction:column;justify-content:center;
  align-items:center;font-weight:900;font-size:15px;line-height:1.35;box-shadow:0 3px 8px rgba(0,0,0,.25)}
.content{position:absolute;left:198px;right:0;top:640px;bottom:0;
  background:linear-gradient(180deg,rgba(255,255,255,0) 0,#fff 40px)}
.tag{position:absolute;left:30px;top:30px;background:var(--green);color:var(--white);font-weight:700;
  font-size:19px;padding:2px 12px;border-radius:4px}
.title{position:absolute;left:30px;top:62px;font-weight:900;color:var(--navy);font-size:64px;line-height:1.08;letter-spacing:-.01em}
.subtitle{position:absolute;left:30px;top:200px;font-weight:700;color:var(--navy);font-size:24px}
.speaker-photo{position:absolute;left:86px;top:244px;width:142px;height:176px;
  background:linear-gradient(180deg,#c9d3dc,#8896a3)}
.details{position:absolute;left:248px;top:244px;list-style:none}
.details li{display:flex;align-items:flex-start;margin-bottom:6px}
.details .key{flex:none;width:44px;background:var(--green);color:var(--white);font-size:14px;font-weight:700;
  text-align:center;border-radius:3px;margin-right:10px;margin-top:5px;padding:1px 0}
.details .val{font-size:21px;font-weight:700;line-height:1.3;color:var(--ink)}
.details small{display:block;font-size:13px;font-weight:500}
.details .name{font-size:30px;font-weight:900}
.contact{position:absolute;left:0;right:0;bottom:12px;text-align:center;color:var(--navy);font-size:14px;line-height:1.5;font-weight:500}
.contact .tel{font-size:24px;font-weight:900;line-height:1.3}
</style>
</head>
<body>
<div class="flyer">
  <div class="scenery" role="img" aria-label="青空と田園風景の写真"></div>
  <div class="route-map" role="img" aria-label="新幹線の路線と駅を示す路線図"></div>

  <p class="catch">地方の実情に合った<br>新幹線の在り方について学ぼう</p>

  <div class="venue-map">
    <p class="label"><span>講演会場</span></p>
    <div class="area" role="img" aria-label="講演会場周辺の案内地図"></div>
  </div>
  <div class="free-badge"><span>申込不要</span><span>入場無料</span></div>

  <section class="content">
    <span class="tag">講演</span>
    <h1 class="title">白峰新幹線実現の<br>可能性を探る</h1>
    <p class="subtitle">〜在来線、ミニ新幹線からフル規格の新幹線へ〜</p>
    <div class="speaker-photo" role="img" aria-label="講師の写真"></div>
    <ul class="details">
      <li><span class="key">講師</span><span class="val"><small>鉄道ジャーナリスト</small><span class="name">柴田 亮</span> 氏</span></li>
      <li><span class="key">とき</span><span class="val">平成28年7月5日(火)<br>午後3時〜</span></li>
      <li><span class="key">ところ</span><span class="val">桐ヶ丘グランドホテル<br>桐ヶ丘市松葉町二丁目3番4号</span></li>
      <li><span class="key">主催</span><span class="val">北辰新幹線青葉延伸推進会議</span></li>
    </ul>
    <div class="contact">
      <p>お問い合わせ</p>
      <p>北辰新幹線青葉延伸推進会議事務局(桐ヶ丘市役所企画課内)</p>
      <p class="tel">Tel 0199-42-8670</p>
    </div>
  </section>
</div>
</body>
</html>
```